Private law enforcement protective services needs a kick ass brochure

We need a brochure that tops the security competition. We are a Pennsylvania based company providing law enforcement officers to the private sector to take the place of regular security officers. We are peacekeepers with the powers of arrest for any major crime committed in our presence. Our customers will get so much more by using our services over regular security. All of our officers attend annual training to stay up to date and sharp in their skills. We would like to see a design that uses the colors Royal blue, black, and grays. The final design should communicate better service over regular security yet have that soft touch and caring feeling. We want to be taken serious yet not scary. We want prospective customers to say WOW... we need to use them rather than regular security guards. We also offer K-9 services. Drug searches as well as explosive searches. THIS NEEDS TO GO ON A TRI FOLD BROCHURE. I already have a website. Www.marlowridgepatrol.com

Target Market(s)

Any business or entity where security or protective services will be needed. We provide services for events like Fairs, carnivals, churches, retail stores, large events, hostile terminations, post disaster sites, overarching of work crews in hostile areas, special celebrations, parades, sporting events,

Industry/Entity Type

Security Service

Font styles to use
Sans Serif

Requirements
Must have
• We need to have a strong professional look yet not too aggressive. DO NOT CALL OUR SERVICES SECURITY !!!! We are PEACEKEEPERS. We Keep the Peace. We provide services all across the state of Pennsylvania. We are one of Pennsylvania's best kept secrets.
Nice to have
• Pictures of Police cars, Officers on patrol at an event,

```html
<!DOCTYPE html>
<html lang="en">
<head>
<meta charset="utf-8">
<title>Marlow Ridge Constable Tri-Fold</title>
<link href="https://fonts.googleapis.com/css2?family=Roboto:ital,wght@0,400;0,500;0,700;1,400&family=Roboto+Condensed:wght@700&display=swap" rel="stylesheet">
<style>
:root{
  --royal:#2e3192;
  --royal-deep:#262a80;
  --ink:#1e1e22;
  --panel-dark:#1b1b1f;
  --text:#4a4a4f;
  --paper:#ffffff;
  --paper-grey:#ececee;
  --bg:#8d8d90;
  --photo-grey:#6f7277;
}
*{margin:0;padding:0;box-sizing:border-box}
html,body{width:917px;height:1200px;overflow:hidden}
body{background:var(--bg);font-family:"Roboto",Arial,sans-serif;color:var(--text);position:relative}
.sheet{position:absolute;left:79px;width:721px;height:510px;box-shadow:0 12px 22px rgba(0,0,0,.35)}
.sheet--outside{top:49px}
.sheet--inside{top:610px;background:linear-gradient(90deg,var(--paper-grey),#fff 45%,var(--paper-grey))}
.panel{position:absolute;top:0;height:510px;width:240px}
.p1{left:0}.p2{left:240px}.p3{left:481px;width:240px}
.body{font-size:6.8px;line-height:9.1px;text-align:justify}
.sub{color:var(--royal);font-weight:500;font-size:8.4px;text-decoration:underline;margin-top:5px;line-height:10px}
.sub:first-child{margin-top:0}
.band{background:var(--royal);color:#fff;font-weight:500;text-align:center;font-size:12.5px;height:26px;line-height:26px;letter-spacing:.2px}
.photo{position:absolute}
.brand{font-family:"Roboto",Arial,sans-serif;font-weight:700;color:var(--royal);text-align:center;letter-spacing:.5px}

/* outside */
.p1.out{background:var(--paper);padding:14px 15px 0 16px}
.p2.out{background:var(--panel-dark);color:#fff}
.p3.out{background:var(--paper);overflow:hidden}
.quote{position:absolute;left:21px;top:250px;width:203px;height:122px;border:1px solid var(--royal);border-radius:9px;text-align:center;padding:22px 10px 0;font-size:6.8px;line-height:9.2px;color:#d8d8dc}
.quote-mark{position:absolute;top:-9px;left:93px;width:17px;height:17px;border-radius:50%;background:var(--royal);color:#fff;font-weight:700;font-size:12px;line-height:20px}
.quote-name{color:var(--royal);font-size:9.8px;margin-top:8px;line-height:10px}
.call{position:absolute;top:380px;width:100%;text-align:center}
.call-now{font-weight:700;font-size:25px;line-height:30px}
.call-phone{font-size:25px;line-height:30px}
.url-pill{display:inline-block;margin-top:6px;background:var(--royal);border-radius:9px;padding:2px 8px;font-weight:700;font-size:12.6px}
.headline{position:absolute;top:311px;width:100%;text-align:center;color:#fff;font-weight:500;font-size:13.6px;line-height:18.4px;padding:0 10px}
.rule{width:78px;height:1px;background:#fff;margin:8px auto 8px;opacity:.8}
.tag{font-style:italic;font-weight:400;font-size:9.8px;line-height:12.5px}
.site{font-family:"Roboto Condensed",Arial,sans-serif;font-weight:700;font-size:9.8px;letter-spacing:.6px;margin-top:14px}

/* inside */
.p1.in{padding:14px 15px 0 19px}
.p2.in{padding:16px 13px 0 15px}
.p3.in{padding:14px 15px 0 16px}
.tps{color:var(--royal);font-weight:500;font-size:9.4px;margin:9px 0 3px}
.footer{position:absolute;left:0;bottom:0;width:721px;height:56px}
.footer-text{position:absolute;bottom:6px;color:#fff;font-weight:500;font-size:14px}
.blue-sub{color:var(--royal);font-weight:500;font-size:8px;line-height:10px;margin-top:6px;text-align:justify}
</style>
</head>
<body>

<section class="sheet sheet--outside">
  <div class="panel p1 out">
    <h3 class="sub">Construction / Utility Job Sites</h3>
    <p class="body">Pennsylvania State Constables can provide over watch for construction crews or utility workers operating in high crime areas. Our constables provide that professional appearance and deterrent required to ward off would be criminals looking for trouble in all the wrong places. If you are working in a dangerous or potentially dangerous area, don't become a statistic. Let our officers provide you with that safe environment needed to successfully complete your job and return home at the end of the day.</p>
    <h3 class="sub">Crowd Control</h3>
    <p class="body">A Pennsylvania State Constable will maintain peace and order where large crowds have gathered. If you are hosting an event and expect a large crowd or a crowd has gathered for whatever reason, don't leave it to a security guard. Let our trained and experienced constables give you added confidence that everything is taken care of.</p>
    <h3 class="sub">Retail</h3>
    <p class="body">Pennsylvania State Constables provide peace keeping services where there is a potential for a crime to be committed. Typical places you will find a constable involving retail with that potential are as follows but not limited to: New product unveiling, black Friday events, book signings, and holiday specials. Call or email us to arrange for one of our constables to serve you today.</p>
    <div class="photo" role="img" aria-label="Photo of two white patrol SUVs parked nose to nose on a town street" style="left:16px;top:263px;width:209px;height:104px;background:linear-gradient(180deg,#b9bfc7,#8a8f96 55%,#5d6168)"></div>
    <div class="band" style="position:absolute;left:16px;top:370px;width:209px">TRAFFIC CONTROL</div>
    <p class="body" style="position:absolute;left:16px;top:402px;width:209px">Two vehicles parked nose to nose aid in providing traffic control by the Marlow Ridge Constable service. Are you having a big event with a large number of attendees? Do you have parking concerns? Is traffic at your event going to be an issue? Our officers are experienced and equipped to handle any traffic detail out there. Whether it's parking concerns, pedestrian foot traffic on roadways, crowd control, events that shut down roadways, or just added traffic to a busy intersection. Let us worry about the issues so you can enjoy your event &amp; have that peace of mind that things are taken care of.</p>
  </div>

  <div class="panel p2 out">
    <div class="photo" role="img" aria-label="Photo of a constable badge and handcuffs on a dark table" style="left:0;top:0;width:240px;height:131px;background:radial-gradient(ellipse at 45% 40%,#6b6256,#2b2a2c 60%,#141416)"></div>
    <div class="brand" style="position:absolute;top:185px;width:100%;font-size:17px;color:#6f78d6">Marlow Ridge</div>
    <div class="quote">
      <div class="quote-mark">&ldquo;</div>
      Our law firm regularly uses the services of Marlow Ridge Constable to serve subpoenas &amp; other legal notices. Their team does a great job at a reasonable price. Sometimes the recipients try and duck service, but their officers work diligently to ensure they are served in a timely &amp; professional manner. We recommend them.
      <div class="quote-name">Dana Whitfield</div>
      <div style="color:#fff">Whitfield Hale Law, P.C</div>
    </div>
    <div class="call">
      <div class="call-now">Call Now!</div>
      <div class="call-phone">(717) 555-0148</div>
      <div class="url-pill">marlowridgepatrol.com</div>
    </div>
  </div>

  <div class="panel p3 out">
    <div class="photo" role="img" aria-label="Photo of a smiling constable in a light blue uniform giving a thumbs up" style="left:16px;top:14px;width:150px;height:300px;background:linear-gradient(180deg,#d5dde8,#a9bbd3 60%,#7f94b5)"></div>
    <div class="brand" style="position:absolute;left:138px;top:80px;width:100px;font-size:14px">Marlow Ridge</div>
    <svg style="position:absolute;left:0;top:0" width="240" height="510" viewBox="0 0 240 510" aria-hidden="true">
      <path d="M0 232 Q40 300 120 292 Q200 284 240 225 L240 510 L0 510 Z" fill="var(--royal)"/>
    </svg>
    <div class="headline">
      A PROVEN LEADER IN PROVIDING PROFESSIONALLY TRAINED &amp; CERTIFIED CONSTABLES THROUGHOUT THE COMMONWEALTH OF PENNSYLVANIA
      <div class="rule"></div>
      <div class="tag">Let our Pennsylvania State Constables<br>give you that peace of mind you deserve</div>
      <div class="site">WWW.MARLOWRIDGEPATROL.COM</div>
    </div>
  </div>
</section>

<section class="sheet sheet--inside">
  <div class="panel p1 in">
    <div class="band" style="font-size:13.6px">CIVIL PROCESS</div>
    <p class="body" style="margin-top:6px">Pennsylvania State Constables are widely utilized to perform various forms of Civil Process. Many private individuals as well as businesses use Constables to serve important private and court-related legal documents. Our Constables will certify your documents were served, as well as give you that added confidence it is handled in a timely manner</p>
    <div class="tps">TYPICAL CIVIL PROCESS SERVED</div>
    <h3 class="sub">Subpoenas</h3>
    <p class="body">A Pennsylvania State Constable is able to serve subpoenas for both private individuals as well as Attorneys and the Court System. Let our constables provide you with the Peace of mind you deserve that everything is taken care of.</p>
    <h3 class="sub">Landlord Tenant</h3>
    <p class="body">A Pennsylvania State Constable is able to serve Landlord Tenant documents to include; 30 day notices, Pay or Quit notices, Eviction hearing notices and Property Recovery Paperwork. Constables also remove tenants still present on a property after the eviction date has been met. These services are provided to private individuals as well as Attorneys and the Court System. Let our constables provide you with the Peace of mind you deserve that everything is taken care of.</p>
    <h3 class="sub">Protection from Abuse ( PFA's )</h3>
    <p class="body">A Pennsylvania State Constable is able to serve PFA's for private individuals, attorneys and for the court system. Constables are not limited by everyday business hours as a sheriff's department or limited availability as a local police department answering emergency calls. If you have an urgent matter that needs immediate attention such as a PFA, let our constables provide you with that peace of mind you deserve.</p>
    <h3 class="sub">Civil Judgements</h3>
    <p class="body">A Pennsylvania State Constable serves civil judgements in cases where the courts have ruled in favor of the plaintiff. Our knowledgeable and experienced constables will assist you with the best outcome possible.</p>
    <h3 class="sub">Domestic Relations</h3>
    <p class="body">A Pennsylvania State Constable serves a magnitude of domestic relations documents to include but not limited to: divorce paperwork, child custody orders, and child support documents. Don't trust just anyone with your important documents, let our professional and experienced constables assist you in this very stressful time.</p>
  </div>

  <div class="panel p2 in">
    <h3 class="sub">Property Recovery</h3>
    <p class="body">A Pennsylvania State Constable is a peace keeper. In situations where personal belongings or property are involved after a messy break up, divorce, or even bad blood between ex roommates, our constables are ready to assist you with a peaceful recovery of those items.</p>
    <h3 class="sub" style="margin-top:9px">Civil Documents</h3>
    <p class="body">A Pennsylvania State Constable serves civil paperwork for private individuals, attorneys, and businesses. These documents include but are not limited to: No Trespass orders, no contact orders, demand letters on past due accounts, notices of impending legal proceedings, Cease and desist orders, and demand letters on rented or leased property. If you have a civil issue and need your very important documents served and certified, let our constables give you that peace of mind you deserve.</p>
    <div class="photo" role="img" aria-label="Photo of a K9 handler with a German shepherd searching a bag" style="left:30px;top:186px;width:120px;height:196px;background:linear-gradient(180deg,#e9e9ec,#a3a5aa 55%,#5a5c62)"></div>
    <div class="brand" style="position:absolute;left:140px;top:240px;width:90px;font-size:13px">Marlow Ridge</div>
    <div class="band" style="position:absolute;left:15px;top:385px;width:210px;font-size:13.6px">K9 SERVICES</div>
    <p class="body" style="position:absolute;left:15px;top:414px;width:210px">We are excited to announce that we now offer K9 services. Our K9s are certified and cross-trained in Narcotics, Explosives, Tracking and Apprehension. Our K9 handlers are trained and experienced. You won't find a more professional K9 service around. Contact us today to find out more about our K9 Services offered.</p>
  </div>

  <div class="panel p3 in">
    <div class="photo" role="img" aria-label="Photo of a constable seen from behind next to a patrol vehicle on a row-house street" style="left:16px;top:14px;width:210px;height:157px;background:linear-gradient(180deg,#b7c6da,#8b7468 45%,#2f3238)"></div>
    <div class="band" style="position:absolute;left:16px;top:175px;width:210px;font-size:13.6px">PEACE KEEPING</div>
    <div style="position:absolute;left:16px;top:207px;width:210px">
      <p class="body">Pennsylvania State Constables are Peace Keepers. A Constable may make a warrant less arrest for any breach of the peace in his or her presence. A breach of the peace by definition in Pennsylvania is any offence that is considered a misdemeanor or felony. Constables work side by side with local and state authorities in many cases around the state. The Pennsylvania State Constable is one of the most overlooked entities around Pennsylvania today. Constables are not security guards, however any where you find event security, you would very easily be able to replace them with a Constable. We are able to function at events and incidents much like a security guard. Our Pennsylvania State Constables will maintain the peace, give you that added presence of law enforcement and peace of mind you deserve.</p>
      <div class="blue-sub">Typical events/locations at which Pennsylvania State Constables provide services:</div>
      <h3 class="sub">Public Events</h3>
      <p class="body">Much like a security guard providing event security, A Pennsylvania State Constable is capable of providing like services and much more. Our constables are a huge deterrent and can act on an individual committing a crime. Some public events you will typically find constables are as follows but not limited to: festivals, fairs, concerts, carnivals, fireworks, large celebrations, Parades, sporting events, car shows and much more.... If you are holding a large event and need peace of mind that you and your guests are safe, let our constables be the ones to provide it for you.</p>
    </div>
  </div>

  <svg class="footer" viewBox="0 0 721 56" preserveAspectRatio="none" aria-hidden="true">
    <path d="M0 4 Q180 30 360 26 Q540 30 721 4 L721 56 L0 56 Z" fill="var(--royal)"/>
  </svg>
  <div class="footer-text" style="left:31px">Call Now! (717) 555-0148</div>
  <div class="footer-text" style="right:22px">marlowridgepatrol.com</div>
</section>

</body>
</html>
```